Funky Modern Flyer A5 or Postcard size

Hi, I am looking at a one small flyer (A5 or postcard size) that I can put both on my website on the front page (ie so png) and also send out if necessary.

It has to be modern, funky and hip. My brand is professional / Corporate so it also has to fit in with that brand.

There are 6 attachments:
Example 1 - FernaPeak - I like this look, clean, modern, funky and says it all.
Example 2 - FernPeak - again another look I like, simple, explanatory
Example 4 - Brightstall Bazaar - font is cool on this one but background not so much too much going on but I like the font
Example 5 - Example 4 - Brightstall Bazaar - font is cool on this one but background not so much too much going on but I like the font
5 is my logo
Example 6 is something I found on the web this morning which is effective.

It is for a Mentoring and Training program I run called: HIGHSTRIDE

What is to be included is the following:
The name: Highstride
Somewhere: Training, Mentoring
My Logo (see attached two options) you can choose which colour suits and I have the source file should you need it
My website and email: www.miriambaskell.example / miriam@miriambaskell.example

This wording: This is one of our highest in-demand programs and is based on a background and proven track record by Miriam in accelerating sales organisations and their people into stand out high performers. **(NOTE this wording in this paragraph may change and I am open to you changing if you think you can make it more effective!)

Colours: white, black and gold (those are our website colours).

I'd like the Highstride to really stand out.... I have included two fonts that I really like that I got off Brightstall Bazaar. However, feel free to suggest other fonts that you think cool or funky!
Updates

Hi everyone, just to add a note to the brief, I am not overly keen on pictures that are really busy. I only like a picture that is minimal and effective. The examples from Brightstall Bazaar was more for the Font Style not so much the pictures in the background. The pictures can take away from a design unless done really minimally.....hope this makes sense. Miriam Added Wednesday, March 15, 2017

Target Market(s)

My target Market is Corporates but I want a Funky Modern look as a lot of people in Corporates are Millennials as well which is part of my target market

Industry/Entity Type

Information Technology

Requirements
Must have
• What is to be included is the following:
• The name: Highstride
• Somewhere: Training, Mentoring
• My Logo (see attached two options) you can choose which colour suits and I have the source file should you need it
• My website and email: www.miriambaskell.example / miriam@miriambaskell.example
• This wording: This is one of our highest in-demand programs and is based on a background and proven track record in high performance and accelerating sales organisations and their people into stand out high performers. (**NOTE this wording may change when final design is picked to be changed as still working in it***)
• Colours: white, black and gold (those are our website colours).
• I'd like the Highstride to really stand out.... I have included two fonts that I really like that I got off Brightstall Bazaar. However, feel free to suggest other fonts that you think cool or funky! NOTE: The pictures I have attached is mainly for the FONTS not for the background pictures. I am not that keen on background pictures as it can take away from the font - unless it is minimal
Should not have
• Too many different colours, I like slick, modern, clean. White, gold and black preferred as this is our website colour.
• NOTE: The pictures from Brightstall Bazaar I have attached are mainly for the FONTS not for the background pictures. I am not hugely keen on background pictures as it can take away from the font/message - unless the pictures are minimal but effective.

```html
<!DOCTYPE html>
<html lang="en">
<head>
<meta charset="utf-8">
<title>Highstride – Training &amp; Mentoring Flyers</title>
<link rel="stylesheet" href="https://fonts.googleapis.com/css2?family=Mr+Dafoe&family=Lato:ital,wght@0,300;0,400;1,300&display=swap">
<style>
  :root {
    --canvas: #ffffff;
    --ink: #000000;
    --gold: #e6b929;
    --gold-soft: #d9ae2c;
    --white: #ffffff;
    --copy: #e9e9e9;
  }
  * { box-sizing: border-box; margin: 0; padding: 0; }
  html, body {
    width: 1200px;
    height: 786px;
    overflow: hidden;
    background: var(--canvas);
  }
  .sheet {
    position: relative;
    width: 1200px;
    height: 786px;
  }
  .flyer {
    position: absolute;
    width: 479px;
    background: var(--ink);
    overflow: hidden;
    color: var(--white);
    font-family: "Lato", Arial, sans-serif;
    text-align: center;
  }
  .flyer--city  { left: 94px;  top: 55px; height: 681px; }
  .flyer--climb { left: 631px; top: 57px; height: 679px; }

  .flyer__photo {
    position: absolute;
    left: 0; top: 0;
    width: 100%;
    height: 440px;
  }
  .flyer--city .flyer__photo {
    background:
      linear-gradient(180deg, rgba(0,0,0,0) 0%, rgba(0,0,0,0) 55%, #000 100%),
      linear-gradient(180deg, #6f6f6f 0%, #8a8a8a 30%, #5a5a5a 62%, #2c2c2c 85%);
  }
  .flyer--climb .flyer__photo {
    background:
      linear-gradient(180deg, rgba(0,0,0,0) 0%, rgba(0,0,0,0) 58%, #000 100%),
      linear-gradient(90deg, rgba(0,0,0,0) 0%, rgba(0,0,0,0) 55%, rgba(30,30,30,0.9) 72%, #3a3a3a 100%),
      radial-gradient(ellipse at 25% 35%, #c9c9c9 0%, #8d8d8d 40%, #4a4a4a 80%);
  }

  .flyer__title {
    position: absolute;
    left: 0; right: 0;
    top: 160px;
    font-family: "Mr Dafoe", "Brush Script MT", cursive;
    font-size: 100px;
    line-height: 1;
    color: var(--gold);
    text-shadow: 0 2px 6px rgba(0,0,0,0.35);
  }
  .flyer--climb .flyer__title { top: 158px; }

  .flyer__services {
    position: absolute;
    left: 0; right: 0;
    top: 292px;
    font-weight: 300;
    font-size: 17px;
    letter-spacing: 0.22em;
    text-transform: uppercase;
    color: var(--white);
  }

  .flyer__pitch {
    position: absolute;
    left: 60px; right: 60px;
    top: 371px;
    font-style: italic;
    font-weight: 300;
    font-size: 14.6px;
    line-height: 25.3px;
    color: var(--copy);
  }

  .flyer__brand {
    position: absolute;
    left: 0; right: 0;
    top: 577px;
    font-weight: 400;
    font-size: 18px;
    letter-spacing: 0.04em;
    text-transform: uppercase;
    color: var(--gold-soft);
  }

  .flyer__contact {
    position: absolute;
    left: 0; right: 0;
    top: 620px;
    font-weight: 300;
    font-size: 13.6px;
    color: var(--white);
  }
</style>
</head>
<body>
<main class="sheet">

  <article class="flyer flyer--city">
    <div class="flyer__photo" role="img" aria-label="Black and white photo of three business people in suits jumping joyfully in front of a city skyline"></div>
    <h1 class="flyer__title">Highstride</h1>
    <p class="flyer__services">Training &amp; Mentoring</p>
    <p class="flyer__pitch">This is one of our highest in-demand programs and is based on a background and proven track record in high performance and accelerating sales organisations and their people into stand out high performers.</p>
    <p class="flyer__brand">Miriam Baskell</p>
    <p class="flyer__contact">www.miriambaskell.example / miriam@miriambaskell.example</p>
  </article>

  <article class="flyer flyer--climb">
    <div class="flyer__photo" role="img" aria-label="Black and white photo of a climber scaling a steep rock face against a cloudy sky"></div>
    <h1 class="flyer__title">Highstride</h1>
    <p class="flyer__services">Training &amp; Mentoring</p>
    <p class="flyer__pitch">This is one of our highest in-demand programs and is based on a background and proven track record in high performance and accelerating sales organisations and their people into stand out high performers.</p>
    <p class="flyer__brand">Miriam Baskell</p>
    <p class="flyer__contact">www.miriambaskell.example / miriam@miriambaskell.example</p>
  </article>

</main>
</body>
</html>
```